Landcape Construction Company needs a flyer to catch attention

A flyer that can be displayed at several different stores detailing our skills, work produced, experience and contact details. Information can be extracted from our website www.brvkw.co.nz. The flyer should feel very green, with addition of pics of work completed as well as stock images of lush green plants, lawns, landscape or similar. Needs to be eye catching with just enough information to express our experience and commitment to high standards

Target Market(s)

Residential
Landscape Architects

Industry/Entity Type

Landscaping

Font styles to use
Serif

Colors
abd037

Requirements
Must have
• Our logo
Experience
Services offered including pictures
All information avail on our website www.brvkw.co.nz
Nice to have
• stock images of lush greenery like a garden after fresh rainfall
Should not have
• Nothing comes to mind

```html
<!DOCTYPE html>
<html lang="en">
<head>
<meta charset="utf-8">
<title>Brookvale Landworks Flyer</title>
<link href="https://fonts.googleapis.com/css2?family=Montserrat:wght@400;500;600;700;900&display=swap" rel="stylesheet">
<style>
  :root {
    --green-dark: #0f7b3b;
    --green-mid: #1e8f3e;
    --green-lime: #abd037;
    --green-lime-deep: #8cc63f;
    --grey-panel: #f1f1f1;
    --page-bg: #e6e6e6;
    --ink: #333333;
    --white: #ffffff;
  }
  * { box-sizing: border-box; margin: 0; padding: 0; }
  html, body { width: 1200px; height: 2301px; overflow: hidden; }
  body { background: var(--page-bg); font-family: "Montserrat", sans-serif; position: relative; }

  .flyer { position: absolute; left: 50px; top: 373px; width: 1100px; height: 1554px; background: var(--white); overflow: hidden; }
  .flyer-shapes { position: absolute; inset: 0; }

  .brand { position: absolute; left: 110px; top: 100px; display: flex; align-items: center; gap: 14px; }
  .brand-dot { width: 44px; height: 44px; border-radius: 50%; background: var(--green-mid); }
  .brand-name { font-family: "Montserrat", sans-serif; font-weight: 700; font-size: 24px; color: var(--green-mid); line-height: 1.1; }

  .headline { position: absolute; left: 63px; top: 335px; color: var(--white); }
  .headline-line { display: block; font-weight: 500; font-size: 64px; line-height: 76px; letter-spacing: 2px; }
  .headline-accent { display: block; font-weight: 900; font-size: 60px; line-height: 78px; color: var(--green-lime); letter-spacing: 1px; }
  .headline-rule { position: absolute; left: 63px; top: 572px; width: 324px; height: 6px; background: var(--white); }

  .intro { position: absolute; left: 88px; top: 780px; width: 400px; font-size: 15.5px; line-height: 22px; color: var(--green-dark); text-align: justify; }

  .services-title { position: absolute; left: 597px; top: 738px; font-weight: 700; font-size: 38px; color: var(--green-dark); letter-spacing: 1px; }
  .services-rule { position: absolute; left: 597px; top: 790px; width: 196px; height: 4px; background: var(--green-dark); }
  .services-text { position: absolute; left: 600px; top: 832px; width: 395px; font-size: 16px; line-height: 22.5px; color: var(--ink); text-align: justify; }

  .work-photo { position: absolute; top: 1100px; width: 267px; height: 156px; border: 3px solid var(--green-dark); }
  .work-photo.decking { left: 65px; background: linear-gradient(180deg, #dff0c0 0%, #a8d37a 55%, #c99a5c 70%, #b07a40 100%); }
  .work-photo.lawn { left: 419px; background: linear-gradient(160deg, #d8d2c4 0%, #9fbf6a 35%, #4f9a2a 70%, #3a7f22 100%); }
  .work-photo.paving { left: 771px; background: linear-gradient(135deg, #9a9a96 0%, #6f706d 50%, #85857f 100%); }

  .service-list { position: absolute; list-style: none; }
  .service-item { position: absolute; display: flex; align-items: center; gap: 10px; width: 160px; font-weight: 600; font-size: 15px; line-height: 16px; color: var(--ink); text-transform: uppercase; }
  .service-icon { flex: 0 0 28px; width: 28px; height: 28px; }

  .footer-call { position: absolute; left: 0; top: 1479px; width: 330px; height: 75px; }
  .call-label { position: absolute; left: 65px; top: 1490px; font-weight: 700; font-size: 22px; color: var(--green-dark); letter-spacing: 1px; }
  .call-number { position: absolute; left: 65px; top: 1518px; font-weight: 600; font-size: 18px; color: var(--green-dark); letter-spacing: 1px; }
  .contact { position: absolute; top: 1505px; display: flex; align-items: center; gap: 10px; font-weight: 600; font-size: 16px; color: var(--white); }
  .contact.email { left: 503px; }
  .contact.web { left: 788px; }
  .contact-divider { position: absolute; left: 733px; top: 1505px; width: 2px; height: 20px; background: var(--white); }
</style>
</head>
<body>
<main class="flyer">
  <svg class="flyer-shapes" viewBox="0 0 1100 1554" width="1100" height="1554">
    <defs>
      <linearGradient id="gardenTone" x1="0" y1="0" x2="1" y2="1">
        <stop offset="0" stop-color="#3f5a3a"/>
        <stop offset="0.4" stop-color="#3e8a2b"/>
        <stop offset="0.75" stop-color="#5fb52c"/>
        <stop offset="1" stop-color="#c9d0c6"/>
      </linearGradient>
      <linearGradient id="greenFade" x1="0" y1="0" x2="1" y2="0">
        <stop offset="0" stop-color="#0f7b3b"/>
        <stop offset="0.45" stop-color="#13803c"/>
        <stop offset="0.72" stop-color="#1e8f3e" stop-opacity="0.35"/>
        <stop offset="0.9" stop-color="#1e8f3e" stop-opacity="0"/>
      </linearGradient>
    </defs>
    <rect x="0" y="0" width="1100" height="1080" fill="url(#gardenTone)" role="img" aria-label="Photo of a lush lawn with hostas and a curved paver path beside a stone wall"/>
    <rect x="0" y="0" width="1100" height="1080" fill="url(#greenFade)"/>
    <path d="M0 262 C380 250 700 170 850 0 H0 Z" fill="#abd037"/>
    <path d="M0 240 C380 228 680 150 800 0 H0 Z" fill="#ffffff"/>
    <path d="M0 862 C200 700 400 628 560 622 C800 618 1000 700 1100 800 V1080 H0 Z" fill="#ffffff"/>
    <path d="M0 882 C200 726 400 652 540 646 V990 Q540 1051 480 1051 H0 Z" fill="#8cc63f"/>
    <rect x="0" y="1074" width="1100" height="405" fill="#f1f1f1"/>
    <polygon points="0,1479 300,1479 320,1554 0,1554" fill="#abd037"/>
    <polygon points="308,1479 1100,1479 1100,1554 328,1554" fill="#0f7b3b"/>
  </svg>

  <div class="brand">
    <span class="brand-dot"></span>
    <span class="brand-name">Brookvale<br>Landworks</span>
  </div>

  <h1 class="headline">
    <span class="headline-line">BROOKVALE</span>
    <span class="headline-line">LANDWORKS</span>
    <span class="headline-accent">COMPANY LIMITED</span>
  </h1>
  <div class="headline-rule"></div>

  <p class="intro">With more than 25 years experience in the landscaping industry, Brookvale Landworks offers services to large or small residential and commercial projects. Based in Canterbury, we are locally owned and operated. Whether you have a blank canvas or are looking to rejuvenate your property we are able to advise and make the process easy and stress free. From paving, pergolas and decks to concrete or planting your dream garden we have the expertise to help.</p>

  <h2 class="services-title">SERVICES</h2>
  <div class="services-rule"></div>
  <p class="services-text">As a full construction landscaping company, we formally offer the following services. However, we regularly work with clients who want something a little out of the box. If there is something in particular you are after, we are happy to discuss options with you.</p>

  <div class="work-photo decking" role="img" aria-label="Photo of timber decking against blurred greenery"></div>
  <div class="work-photo lawn" role="img" aria-label="Photo of a sprinkler watering a lawn beside a path"></div>
  <div class="work-photo paving" role="img" aria-label="Photo of grey concrete paving"></div>

  <ul class="service-list">
    <li class="service-item" style="left:65px;top:1297px"><svg class="service-icon" viewBox="0 0 28 28"><circle cx="14" cy="14" r="14" fill="#0f7b3b"/><rect x="8" y="9" width="12" height="10" rx="2" fill="none" stroke="#fff" stroke-width="2"/></svg>Patios</li>
    <li class="service-item" style="left:212px;top:1297px"><svg class="service-icon" viewBox="0 0 28 28"><circle cx="14" cy="14" r="14" fill="#0f7b3b"/><path d="M14 7 C10 12 9 15 14 20 C19 15 18 12 14 7Z" fill="#fff"/></svg>Water<br>Features</li>
    <li class="service-item" style="left:65px;top:1351px"><svg class="service-icon" viewBox="0 0 28 28"><circle cx="14" cy="14" r="14" fill="#0f7b3b"/><path d="M8 8h12v12H8z M8 14h12 M14 8v12" fill="none" stroke="#fff" stroke-width="2"/></svg>Paving</li>
    <li class="service-item" style="left:212px;top:1351px"><svg class="service-icon" viewBox="0 0 28 28"><circle cx="14" cy="14" r="14" fill="#0f7b3b"/><path d="M7 11h14 M7 15h14 M7 19h14" stroke="#fff" stroke-width="2"/></svg>Decking</li>
    <li class="service-item" style="left:65px;top:1403px"><svg class="service-icon" viewBox="0 0 28 28"><circle cx="14" cy="14" r="14" fill="#0f7b3b"/><path d="M8 20h12 M10 20V11h8v9" fill="none" stroke="#fff" stroke-width="2"/></svg>Concrete</li>

    <li class="service-item" style="left:420px;top:1297px"><svg class="service-icon" viewBox="0 0 28 28"><circle cx="14" cy="14" r="14" fill="#0f7b3b"/><path d="M9 20V9 M14 20V8 M19 20V9 M7 12h14 M7 17h14" stroke="#fff" stroke-width="2"/></svg>Fencing</li>
    <li class="service-item" style="left:557px;top:1297px"><svg class="service-icon" viewBox="0 0 28 28"><circle cx="14" cy="14" r="14" fill="#0f7b3b"/><path d="M8 13h12l-2 7h-8z M14 13V8" fill="none" stroke="#fff" stroke-width="2"/></svg>Planter<br>Boxes</li>
    <li class="service-item" style="left:420px;top:1351px"><svg class="service-icon" viewBox="0 0 28 28"><circle cx="14" cy="14" r="14" fill="#0f7b3b"/><path d="M8 8h12v12H8z M8 12h12 M8 16h12" fill="none" stroke="#fff" stroke-width="2"/></svg>Board<br>Walks</li>
    <li class="service-item" style="left:557px;top:1351px"><svg class="service-icon" viewBox="0 0 28 28"><circle cx="14" cy="14" r="14" fill="#0f7b3b"/><path d="M7 10h14 M10 10v10 M18 10v10" stroke="#fff" stroke-width="2"/></svg>Pergolas</li>
    <li class="service-item" style="left:420px;top:1403px"><svg class="service-icon" viewBox="0 0 28 28"><circle cx="14" cy="14" r="14" fill="#0f7b3b"/><rect x="8" y="10" width="12" height="8" fill="none" stroke="#fff" stroke-width="2"/></svg>Timber</li>

    <li class="service-item" style="left:760px;top:1297px"><svg class="service-icon" viewBox="0 0 28 28"><circle cx="14" cy="14" r="14" fill="#0f7b3b"/><path d="M7 9h14v10H7z M7 14h14 M12 9v5 M16 14v5" fill="none" stroke="#fff" stroke-width="2"/></svg>Retaining<br>Walls</li>
    <li class="service-item" style="left:920px;top:1297px"><svg class="service-icon" viewBox="0 0 28 28"><circle cx="14" cy="14" r="14" fill="#0f7b3b"/><path d="M8 18 Q14 6 20 18" fill="none" stroke="#fff" stroke-width="2"/></svg>Irrigat<br>ion</li>
    <li class="service-item" style="left:760px;top:1351px"><svg class="service-icon" viewBox="0 0 28 28"><circle cx="14" cy="14" r="14" fill="#0f7b3b"/><path d="M14 20V12 M14 14 Q9 13 9 8 Q14 9 14 14 M14 14 Q19 13 19 8 Q14 9 14 14" fill="none" stroke="#fff" stroke-width="1.8"/></svg>Gardens &amp;<br>Lawns</li>
    <li class="service-item" style="left:920px;top:1351px"><svg class="service-icon" viewBox="0 0 28 28"><circle cx="14" cy="14" r="14" fill="#0f7b3b"/><path d="M8 9h12v8h-7l-4 3v-3H8z" fill="none" stroke="#fff" stroke-width="2"/></svg>Consult<br>ation</li>
    <li class="service-item" style="left:760px;top:1403px;width:200px"><svg class="service-icon" viewBox="0 0 28 28"><circle cx="14" cy="14" r="14" fill="#0f7b3b"/><path d="M9 8h10v12H9z M11 12h6 M11 16h6" fill="none" stroke="#fff" stroke-width="2"/></svg>Project<br>Management</li>
  </ul>

  <p class="call-label">CALL US</p>
  <p class="call-number">021 555 0148</p>

  <p class="contact email"><svg width="20" height="14" viewBox="0 0 20 14"><rect x="1" y="1" width="18" height="12" fill="none" stroke="#fff" stroke-width="2"/><path d="M1 1l9 7 9-7" fill="none" stroke="#fff" stroke-width="2"/></svg>hello@brvkw.co.nz</p>
  <span class="contact-divider"></span>
  <p class="contact web"><svg width="18" height="18" viewBox="0 0 18 18"><circle cx="9" cy="9" r="8" fill="none" stroke="#fff" stroke-width="1.8"/><ellipse cx="9" cy="9" rx="3.5" ry="8" fill="none" stroke="#fff" stroke-width="1.5"/><path d="M1 9h16" stroke="#fff" stroke-width="1.5"/></svg>brvkw.co.nz.</p>
</main>
</body>
</html>
```